Brightpath Dentistry - Flyer - Modern & Eye catching campaign flyer

Need front & back side full page flyer designs for both 1) Grand opening 2) On-going campaign.

Attached the new dental office logo.
Attached our other dental clinic flyer designs for content.

Target Market(s)

Cosmetic dentistry

Industry/Entity Type

Health Care

Requirements
Must have
• decent, modern and eye catching marketing flyers.
Nice to have
• - Nice space
• - Highlight phone number
• - Highlight special features like convenient hours, call or text, for all ages, digital facility, etc
Should not have
• - Don't want to fill the flyer with too much wordings
• - Too many colors

```html
<!DOCTYPE html>
<html lang="en">
<head>
<meta charset="utf-8">
<title>Brightpath Dentistry – Grand Opening Specials</title>
<link rel="stylesheet" href="https://fonts.googleapis.com/css2?family=Poppins:wght@500;600;700&family=Open+Sans:wght@600;700&display=swap">
<style>
  :root {
    --green: #3dba74;
    --green-deep: #5a8a3c;
    --green-light: #6cc067;
    --ring-blue: #4a70b5;
    --label-blue: #4566b5;
    --band-text: #4a55a8;
    --sky: #29b5e8;
    --orange: #dc8a2c;
    --ink: #111111;
    --white: #ffffff;
    --photo-a: #f4f6f7;
    --photo-b: #d9dfe2;
  }
  * { box-sizing: border-box; margin: 0; padding: 0; }
  html, body { width: 848px; height: 1200px; overflow: hidden; background: var(--white); }
  .flyer {
    position: relative; width: 848px; height: 1200px; overflow: hidden;
    background: var(--white);
    font-family: "Open Sans", Arial, sans-serif;
  }
  .backdrop-photo {
    position: absolute; left: 0; top: 180px; width: 848px; height: 840px;
    background: radial-gradient(ellipse at 45% 55%, var(--photo-b) 0%, var(--photo-a) 70%, var(--white) 100%);
  }
  .shapes { position: absolute; inset: 0; }
  .brand {
    position: absolute; left: 34px; top: 96px;
    font-family: "Poppins", sans-serif; font-weight: 600; font-size: 34px; line-height: 1.1;
    color: var(--sky);
  }
  .headline {
    position: absolute; left: 20px; top: 288px;
    font-family: "Poppins", sans-serif; font-weight: 700; font-size: 53px; letter-spacing: -1.5px;
    color: var(--ink); line-height: 1;
  }
  .headline-sub {
    position: absolute; left: 49px; top: 350px;
    font-family: "Poppins", sans-serif; font-weight: 700; font-size: 50px; letter-spacing: -1.5px;
    color: var(--sky); line-height: 1;
  }
  .perks { position: absolute; left: 25px; top: 404px; list-style: none; }
  .perks li {
    font-family: "Poppins", sans-serif; font-weight: 500; font-size: 29.5px;
    color: var(--ink); line-height: 52px; letter-spacing: -0.6px;
  }
  .price-tag {
    position: absolute; height: 52px; padding: 0 10px; border-radius: 26px;
    background: var(--orange); color: var(--white);
    font-weight: 700; font-size: 30px; line-height: 52px; z-index: 2;
  }
  .offer-band {
    position: absolute; left: 0; height: 58px; border-radius: 0 29px 29px 0;
    background: var(--green); color: var(--band-text);
    font-weight: 700; font-size: 33px; line-height: 58px; letter-spacing: -0.5px;
  }
  .reg-price {
    position: absolute; left: 0; width: 444px; text-align: center;
    font-weight: 700; font-size: 16px; color: var(--label-blue);
  }
  .included { position: absolute; font-weight: 600; font-size: 13px; color: var(--label-blue); display: flex; align-items: center; gap: 5px; }
  .included svg { width: 22px; height: 20px; }
  .service {
    position: absolute; font-weight: 700; font-size: 26px; line-height: 30px;
    color: var(--label-blue); text-align: center; white-space: nowrap;
  }
  .footer-note {
    position: absolute; left: 15px; top: 1156px;
    font-weight: 600; font-size: 25px; color: var(--ink);
  }
</style>
</head>
<body>
<main class="flyer">
  <div class="backdrop-photo" role="img" aria-label="Faint photo of a whitening syringe, a clear aligner and an open hand in a dental clinic"></div>

  <svg class="shapes" width="848" height="1200" viewBox="0 0 848 1200" aria-hidden="true">
    <defs>
      <linearGradient id="topWave" x1="0" y1="0" x2="1" y2="0">
        <stop offset="0" stop-color="#2d9be0"/>
        <stop offset="0.3" stop-color="#2fbf9c"/>
        <stop offset="1" stop-color="#3dba74"/>
      </linearGradient>
      <linearGradient id="bottomWave" x1="0" y1="0" x2="1" y2="0">
        <stop offset="0" stop-color="#1a9e74"/>
        <stop offset="0.4" stop-color="#2ebc6f"/>
        <stop offset="1" stop-color="#7cc75e"/>
      </linearGradient>
    </defs>
    <path d="M300 0 H848 V175 C700 110 480 40 300 0 Z" fill="url(#topWave)"/>
    <path d="M300 28 C480 50 700 110 848 175 V160 C700 100 480 35 310 20 Z" fill="var(--green-deep)"/>
    <path d="M0 985 C250 1085 550 1135 848 1150 V1200 H0 Z" fill="url(#bottomWave)"/>
    <path d="M0 985 C250 1085 550 1135 848 1150 V1162 C550 1147 250 1097 0 1000 Z" fill="var(--green-deep)"/>
    <circle cx="100" cy="60" r="215" fill="var(--white)" stroke="var(--sky)" stroke-width="6"/>
    <polyline points="462,72 462,166 481,293 502,418 534,545 567,671 577,797 596,924 570,1050 530,1125"
      fill="none" stroke="var(--green)" stroke-width="20" stroke-linejoin="round"/>
    <g fill="var(--green-light)" stroke="var(--ring-blue)" stroke-width="9">
      <circle cx="470" cy="166" r="48"/>
      <circle cx="481" cy="293" r="48"/>
      <circle cx="502" cy="418" r="48"/>
      <circle cx="534" cy="545" r="48"/>
      <circle cx="567" cy="671" r="48"/>
      <circle cx="577" cy="797" r="48"/>
      <circle cx="596" cy="924" r="48"/>
      <circle cx="570" cy="1050" r="48"/>
    </g>
  </svg>

  <div class="brand">Brightpath<br>Dentistry</div>

  <h1 class="headline">Grand Opening</h1>
  <h2 class="headline-sub">Specials</h2>
  <ul class="perks">
    <li>Free kids dental</li>
    <li>$25 Adults dental Screening</li>
    <li>15% off on Treatment plan</li>
  </ul>

  <div class="price-tag" style="left:10px;top:564px;">$59/-</div>
  <div class="offer-band" style="top:603px;width:356px;padding-left:23px;">New Patient Special</div>
  <div class="included" style="left:128px;top:668px;"><svg viewBox="0 0 22 20"><rect x="1" y="5" width="14" height="14" fill="none" stroke="#dc8a2c" stroke-width="2"/><path d="M4 11 L8 15 L20 2" fill="none" stroke="#dc8a2c" stroke-width="3"/></svg>EXAM</div>
  <div class="included" style="left:220px;top:668px;"><svg viewBox="0 0 22 20"><rect x="1" y="5" width="14" height="14" fill="none" stroke="#dc8a2c" stroke-width="2"/><path d="M4 11 L8 15 L20 2" fill="none" stroke="#dc8a2c" stroke-width="3"/></svg>DIGITAL X-RAYS</div>
  <div class="included" style="left:128px;top:701px;"><svg viewBox="0 0 22 20"><rect x="1" y="5" width="14" height="14" fill="none" stroke="#dc8a2c" stroke-width="2"/><path d="M4 11 L8 15 L20 2" fill="none" stroke="#dc8a2c" stroke-width="3"/></svg>CLEANING</div>

  <div class="price-tag" style="left:10px;top:705px;">$246/-</div>
  <div class="offer-band" style="top:748px;width:440px;padding-left:15px;">In-Office Teeth Whitening</div>
  <div class="reg-price" style="top:813px;">(REG. PRICE $500)</div>

  <div class="price-tag" style="left:10px;top:850px;padding:0 12px;">$695/-</div>
  <div class="offer-band" style="top:893px;width:489px;text-align:center;">Veneers /Purelays</div>
  <div class="reg-price" style="top:957px;">(REG. PRICE $995)</div>

  <div class="service" style="left:538px;top:153px;">DENTURES</div>
  <div class="service" style="left:559px;top:267px;">NIGHT<br>GUARDS</div>
  <div class="service" style="left:565px;top:403px;">EXTRACTIONS</div>
  <div class="service" style="left:604px;top:530px;">VENEERS</div>
  <div class="service" style="left:622px;top:641px;">CROWN AND<br>BRIDGE</div>
  <div class="service" style="left:640px;top:782px;">IMPLANTS</div>
  <div class="service" style="left:657px;top:897px;">ROOT CANAL<br>THERAPY</div>
  <div class="service" style="left:627px;top:1030px;">CLEARALIGN<br>(Invisible braces)</div>

  <p class="footer-note">Offer expires in 30 days. New patients are welcome!</p>
</main>
</body>
</html>
```